National Attorney Referal Biz Needs a Flyer Design by a Pro

The Harbor Roster is a 114 year old company based in Bismarck, ND, USA. We are looking to have a flyer designed that we can attach into email communications as well as have printed.
Visit us at www.HarborRoster.example to see more about what we do.
Essentially our attorney members pay us an annual membership fee and in return we provide them business. This flyer will be used to attract new business who have outstanding debt that needs to be collected upon by our collection attorneys.
Attached is a hand drawn example of what I am looking for. Our logo is also attached which should be used in the flyer. Our colors are blue and silver/grey just like the logo.
There is one thing that I need you to add to the flyer. In the center you will see the word FREE. Next to the last E should be an asterix*. At the bottom of the flyer there should be an asterix* as well saying
*Should you chose to file suit then fees would be incurred.

Target Market(s)

Associations that have members. For example an apartment association, pest management association, or any other labor based organization. We also want to send this directly to small to medium sized business owners.

Industry/Entity Type

Communications

Font styles to use
Sans Serif

Colors
3276b5
86cae6
0355a3

Requirements
Must have
• compelling visual graphics. It should also be easy to read.
Nice to have
• Inviting color that complements our logo.
• I am unsure of what font would work best. You decide.

```html
<!DOCTYPE html>
<html lang="en">
<head>
<meta charset="utf-8">
<title>The Harbor Roster of Attorneys – Free Collection Flyer</title>
<link href="https://fonts.googleapis.com/css2?family=Oswald:wght@500;600&family=Open+Sans:wght@400;600;700&display=swap" rel="stylesheet">
<style>
  :root {
    --brand-blue: #3276b5;
    --brand-deep: #0355a3;
    --brand-sky: #86cae6;
    --navy-ink: #1d2b63;
    --header-tint: #d3e3f3;
    --paper: #eef3f8;
    --ring: #7cc0e4;
    --swoosh: #dde4ec;
    --bubble: #a8d8f0;
    --silver: #b7c0cb;
    --page-bg: #e9e9e9;
  }
  * { box-sizing: border-box; margin: 0; padding: 0; }
  html, body { width: 977px; height: 1200px; overflow: hidden; background: var(--page-bg); }
  .flyer {
    position: relative; width: 977px; height: 1200px; background: var(--paper);
    font-family: "Open Sans", sans-serif; color: var(--navy-ink); overflow: hidden;
  }
  .masthead {
    position: absolute; inset: 0 0 auto 0; height: 183px; background: var(--header-tint);
    border-bottom: 4px solid var(--brand-sky);
    display: flex; flex-direction: column; align-items: center; padding-top: 22px;
  }
  .brand-mark {
    width: 70px; height: 70px; border-radius: 50%;
    border: 5px solid var(--silver); background: #fff;
  }
  .brand-name { margin-top: 10px; font-weight: 700; font-size: 22px; line-height: 1.05; text-align: center; color: var(--navy-ink); }
  .brand-tagline { margin-top: 6px; font-size: 11px; text-align: center; line-height: 1.3; }
  .cycle { position: absolute; left: 0; top: 183px; width: 977px; height: 860px; }
  .art {
    position: absolute; border-radius: 10px;
  }
  .art--owner { left: 438px; top: 262px; width: 100px; height: 130px; background: linear-gradient(#c9b49b, #1f3550); }
  .art--cash { left: 175px; top: 520px; width: 130px; height: 95px; background: linear-gradient(#6f9a63, #3f6b3a); }
  .art--court { left: 425px; top: 770px; width: 130px; height: 120px; background: linear-gradient(#e4c65a 0%, #f4f1ea 35%, #1f3550 100%); }
  .partner-spot {
    position: absolute; left: 680px; top: 530px; width: 110px; display: flex; flex-direction: column; align-items: center; gap: 6px;
  }
  .partner-spot .dot { width: 70px; height: 70px; border-radius: 50%; border: 5px solid var(--silver); background: #fff; }
  .partner-spot span { font-size: 12px; font-weight: 700; text-align: center; }
  .bubble {
    position: absolute; background: var(--bubble); border-radius: 8px;
    font-size: 12.5px; line-height: 1.35; text-align: center; padding: 8px 12px;
  }
  .bubble--1 { left: 368px; top: 404px; width: 240px; }
  .bubble--2 { left: 650px; top: 660px; width: 240px; }
  .bubble--3 { left: 318px; top: 900px; width: 340px; }
  .bubble--4 { left: 95px; top: 626px; width: 250px; }
  .free-word {
    position: absolute; left: 0; right: 0; top: 566px; text-align: center;
    font-family: "Oswald", sans-serif; font-weight: 600; font-size: 84px; letter-spacing: 1px; color: var(--navy-ink);
  }
  .free-word sup { font-size: 40px; vertical-align: 34px; }
  .footnote {
    position: absolute; left: 0; right: 0; top: 1050px; text-align: center; font-size: 12px; font-style: italic;
  }
  .contact-band {
    position: absolute; left: 0; right: 0; bottom: 0; height: 114px; background: var(--brand-blue);
    color: #fff; text-align: center; padding-top: 10px;
  }
  .contact-phone { font-family: "Oswald", sans-serif; font-weight: 500; font-size: 40px; line-height: 1.1; }
  .contact-visit { font-size: 14px; }
  .contact-web { font-family: "Oswald", sans-serif; font-weight: 500; font-size: 24px; letter-spacing: 1px; }
</style>
</head>
<body>
<main class="flyer">
  <header class="masthead">
    <div class="brand-mark" aria-hidden="true"></div>
    <div class="brand-name">The Harbor Roster<sup>®</sup><br>of Attorneys</div>
    <p class="brand-tagline">Worldwide Legal Referrals to the<br>Credit Industry Since 1900</p>
  </header>

  <svg class="cycle" viewBox="0 183 977 860" aria-hidden="true">
    <ellipse cx="488" cy="606" rx="330" ry="240" fill="none" stroke="var(--swoosh)" stroke-width="26" transform="rotate(-35 488 606)"/>
    <ellipse cx="488" cy="606" rx="300" ry="200" fill="none" stroke="var(--swoosh)" stroke-width="14" transform="rotate(-35 488 606)"/>
    <circle cx="488" cy="606" r="250" fill="none" stroke="var(--ring)" stroke-width="5"/>
    <g fill="#fff" stroke="var(--ring)" stroke-width="3" font-family="Open Sans, sans-serif" font-size="14" font-weight="700">
      <circle cx="664" cy="429" r="14"/><circle cx="713" cy="718" r="14"/>
      <circle cx="488" cy="856" r="14"/><circle cx="265" cy="490" r="14"/>
    </g>
    <g fill="var(--navy-ink)" font-family="Open Sans, sans-serif" font-size="14" font-weight="700" text-anchor="middle">
      <text x="664" y="434">1</text><text x="713" y="723">2</text>
      <text x="488" y="861">3</text><text x="265" y="495">4</text>
    </g>
  </svg>

  <div class="art art--owner" role="img" aria-label="Illustrated business owner in a suit"></div>
  <div class="art art--cash" role="img" aria-label="Illustrated stack of banknotes"></div>
  <div class="art art--court" role="img" aria-label="Illustrated attorney in front of a courthouse"></div>
  <div class="partner-spot"><div class="dot" aria-hidden="true"></div><span>The Harbor Roster</span></div>

  <p class="bubble bubble--1">Your business performed to end of agreement. But your customer did not pay you.</p>
  <p class="bubble bubble--2">Visit www.HarborRoster.example or call and submit your claim so that you can get paid.</p>
  <p class="bubble bubble--3">One of our 1,000+ screened collection attorneys will be assigned your claim in the debtor's backyard to collect your money. We have collection attorneys in every geography. The cost to you is zilch, zero, nada, in other words free.</p>
  <p class="bubble bubble--4">We assist in collecting your money for you. A small percentage of the amount collected pays our attorney. The balance goes to you.</p>

  <div class="free-word">FREE<sup>*</sup></div>

  <p class="footnote">*Should you chose to file suit then fees would be incurred.</p>

  <footer class="contact-band">
    <div class="contact-phone">800-555-0142</div>
    <div class="contact-visit">Visit us at</div>
    <div class="contact-web">WWW.HARBORROSTER.EXAMPLE</div>
  </footer>
</main>
</body>
</html>
```